依頼概要
■依頼目的/概要

電子書籍のための
表紙デザイン作成をお願いいたします。

PDFとして、配布する予定です。

■納品物

下記での納品をお願いいたします。

JPEG形式
A5サイズで納まるサイズ

■本の内容

<本のタイトル>
人生を変えたいあなたへ

<副タイトル>
望む人生を手に入れる5つの秘訣

<キャッチコピー>

以下の文言の中から組み合わせでお願いします

・なぜ人生を変えたいと思うのに変えれないのか?
・大切なのは家などの外部環境とあなたの心の内部環境
・動画配信 24万人超「木漏れ日ひろばチャンネル」

<著書名>

・著者名 ライフデザインの専門家 棚橋周平

■デザイン要望

・本のタイトル/キャッチコピー/著書名の反映をお願い致します。

・読者は40代以上の女性がメイン

・拙著「陽だまり小径」のデザインを、それとなく取り入れてください

<表現したいイメージなど>

・信頼感

・40代以上の女性が手に取りたくなるデザイン

・ベストセラーの自己啓発書など、
どこかで見たことがあるような感じの安心感

・カラーの希望などはありません。お任せで。

<利用画像について>

イラスト等素材を使用される場合には、
商用利用可の素材をお願いします。

■その他、デザインを考えるのに必要な情報などありましたら、

お答えしますので、遠慮なく聞いて下さい。
■ 選んだ理由

この度はたくさんのご応募ありがとうございました。拙著「陽だまり小径」をベースにというお願いをしたところ、そのイメージ近いものから、さらに飛躍させた案まで出てきて非常にありがたく思っています。
当選案を選ぶには非常に悩みました。次点の方やその他の方の案もいいものが多くあったのですが、最終的には目立ちながらやさしい感じがすることとタイトルとキャッチコピーの視認性で選定させていただきました。

■ 提案者全員のお礼・コメント

みなさま、この度はご提案ありがとうございました。当選と次点を選ばせていただきましたが、それ以外にも素敵な案がたくさんあり、非常に選定に悩んだのが実際のところです。
当選案は、私がお伝えしていたイメージからさらに飛躍していただいたものにさせていただきました。色を変えてシリーズ化できそうなところなど今後の展開もイメージできそうです。
他の方の案に関しても素敵なものが多かったので、他のシリーズの電子書籍などを出す場合は、個別に依頼させていただく可能性もありますので、これをご縁によろしくお願いします。

```html
<!DOCTYPE html>
<html lang="ja">
<head>
<meta charset="utf-8">
<title>人生を変えたいあなたへ</title>
<link rel="stylesheet" href="https://fonts.googleapis.com/css2?family=Noto+Sans+JP:wght@400;500;700;900&display=swap">
<style>
  :root {
    --ink: #1a1a1a;
    --rose: #c98a8f;
    --rose-line: #e3b7b9;
    --badge: #d58e93;
    --badge-gold: #fff3c0;
    --sand: #dcc4a8;
    --sand-deep: #cfb292;
    --brown: #4a3426;
    --paper: #ffffff;
  }
  html, body { margin: 0; padding: 0; overflow: hidden; background: var(--paper); }
  .cover {
    position: relative; width: 847px; height: 1200px; overflow: hidden;
    background: var(--paper);
    font-family: "Noto Sans JP", sans-serif; color: var(--ink);
  }
  .title-line {
    position: absolute; left: 130px; margin: 0;
    font-weight: 900; font-size: 150px; line-height: 1;
  }
  .title-1 { top: 52px; letter-spacing: 32px; }
  .title-2 { top: 322px; letter-spacing: 4px; }
  .title-3 { top: 582px; letter-spacing: 8px; }
  .rule {
    position: absolute; left: 70px; width: 700px; height: 3px;
    border-top: 1px solid var(--rose-line); border-bottom: 1px solid var(--rose-line);
  }
  .subtitle {
    position: absolute; margin: 0; color: var(--rose);
    font-weight: 700; font-size: 46px; line-height: 1; letter-spacing: 3px;
  }
  .subtitle-1 { left: 240px; top: 260px; }
  .subtitle-2 { left: 420px; top: 527px; }
  .badge {
    position: absolute; left: 108px; top: 750px; width: 170px; height: 170px;
    border-radius: 50%; background: var(--badge); color: #fff; z-index: 2;
    display: flex; flex-direction: column; align-items: center; justify-content: center;
    text-align: center; line-height: 1.15;
  }
  .badge-label { font-size: 16px; font-weight: 700; }
  .badge-count { font-size: 50px; font-weight: 900; color: var(--badge-gold); line-height: 1; margin: 2px 0; }
  .badge-count small { font-size: 20px; }
  .badge-channel { font-size: 12px; font-weight: 700; width: 130px; }
  .author { position: absolute; right: 30px; top: 780px; text-align: right; }
  .author-role { font-size: 17px; font-weight: 500; margin: 0 0 14px; }
  .author-name { font-size: 38px; font-weight: 500; letter-spacing: 8px; margin: 0; }
  .band { position: absolute; left: 0; top: 880px; width: 847px; height: 320px; }
  .band-art { position: absolute; left: 60px; top: 960px; width: 720px; height: 200px; opacity: .25;
    background: linear-gradient(90deg, var(--sand-deep), transparent 40%, transparent 60%, var(--sand-deep)); }
  .question {
    position: absolute; left: 40px; top: 1010px; margin: 0; color: var(--brown);
    font-weight: 700; font-size: 28px; line-height: 1.4;
  }
  .question .big { display: block; font-size: 42px; font-weight: 900; }
  .message {
    position: absolute; left: 490px; top: 960px; margin: 0; color: var(--brown);
    font-weight: 700; font-size: 28px; line-height: 1.3;
  }
  .message .big { font-size: 46px; font-weight: 900; }
</style>
</head>
<body>
<main class="cover">
  <h1 class="title-line title-1">人生を</h1>
  <div class="rule" style="top:238px"></div>
  <p class="subtitle subtitle-1">望む人生を手に入れる</p>
  <div class="rule" style="top:328px"></div>
  <p class="title-line title-2">変えたい</p>
  <div class="rule" style="top:513px"></div>
  <p class="subtitle subtitle-2">5つの秘訣</p>
  <div class="rule" style="top:600px"></div>
  <p class="title-line title-3">あなたへ</p>

  <div class="badge">
    <span class="badge-label">動画配信<br>登録者</span>
    <span class="badge-count">24<small>万人超</small></span>
    <span class="badge-channel">「木漏れ日ひろば<br>チャンネル」</span>
  </div>

  <div class="author">
    <p class="author-role">ライフデザインの専門家</p>
    <p class="author-name">棚橋周平</p>
  </div>

  <svg class="band" viewBox="0 0 847 320" preserveAspectRatio="none" aria-hidden="true">
    <path d="M0 40 Q 212 0 423 30 T 847 20 V320 H0 Z" fill="var(--sand)"/>
  </svg>
  <div class="band-art" role="img" aria-label="淡い線画の家並みのイラスト"></div>

  <p class="question">なぜ人生を<br>変えたいと思うのに<span class="big">―変えれないのか?</span></p>
  <p class="message">大切なのは家などの<br><span class="big">外部環境</span>と<br>あなたの心の<br><span class="big">内部環境</span></p>
</main>
</body>
</html>
```